Business Card for Willowcrest Terrain Advisors

We need a business card for Willowcrest Terrain Advisors. The company website address is provided below. The company logo is attached. We provide specialized permafrost services to the mining, transportation, and oil & gas industries. The card should be prepared for:
Dominic Halloway, PhD.
Willowcrest Terrain Advisors
PO Box 418529
Birch Hollow, Alaska 99612
Direct: +1-907-555-2964
Email: dhalloway@terrainadvisors-example.com
Website: www.willowcrestterrainadvisors-example.com

```html
<!DOCTYPE html>
<html lang="en">
<head>
<meta charset="utf-8">
<title>Willowcrest Terrain Advisors — Business Card</title>
<link rel="stylesheet" href="https://fonts.googleapis.com/css2?family=Montserrat:wght@400;700&display=swap">
<style>
  :root {
    --backdrop: #2b2b2e;
    --card: #ffffff;
    --ink: #1c2026;
    --ink-soft: #3a3f46;
    --accent-bar: #111418;
  }
  * { box-sizing: border-box; margin: 0; padding: 0; }
  html, body {
    width: 1200px; height: 913px; overflow: hidden;
    background: var(--backdrop);
    font-family: "Montserrat", Arial, sans-serif;
  }
  .stage {
    width: 1200px; height: 913px;
    display: flex; flex-direction: column;
    align-items: center; justify-content: center; gap: 40px;
  }
  .card {
    position: relative;
    width: 700px; height: 400px;
    background: var(--card);
    border-radius: 26px;
    color: var(--ink);
    overflow: hidden;
  }
  /* Front */
  .card--front {
    display: flex; align-items: center; justify-content: center;
  }
  .brand-name {
    font-weight: 700;
    color: var(--ink);
    letter-spacing: 0.02em;
  }
  .card--front .brand-name { font-size: 36px; }

  /* Back */
  .card--back .brand-name {
    position: absolute; left: 44px; top: 52px;
    font-size: 20px;
  }
  .holder {
    position: absolute; right: 44px; top: 44px;
    text-align: right;
  }
  .holder__name { font-weight: 700; font-size: 20px; color: var(--ink); }
  .holder__company { font-size: 16px; color: var(--ink-soft); margin-top: 4px; }
  .holder-bar {
    position: absolute; right: 0; top: 40px;
    width: 14px; height: 58px;
    background: var(--accent-bar);
  }
  .address {
    position: absolute; left: 44px; top: 210px;
    font-size: 17px; line-height: 1.5; color: var(--ink-soft);
  }
  .contact-list {
    position: absolute; left: 44px; top: 286px;
    list-style: none;
    font-size: 16px; line-height: 1; color: var(--ink-soft);
  }
  .contact-list li {
    display: flex; align-items: center; gap: 12px;
    height: 30px;
  }
  .contact-list svg { width: 16px; height: 16px; flex: none; fill: var(--ink); }
</style>
</head>
<body>
<main class="stage">
  <section class="card card--front" aria-label="Card front">
    <span class="brand-name">Willowcrest Terrain Advisors</span>
  </section>

  <section class="card card--back" aria-label="Card back">
    <span class="brand-name">Willowcrest Terrain Advisors</span>

    <div class="holder">
      <p class="holder__name">Dominic Halloway, PhD</p>
      <p class="holder__company">Willowcrest Terrain Advisors</p>
    </div>
    <span class="holder-bar"></span>

    <address class="address" style="font-style:normal">
      PO Box 418529<br>
      Birch Hollow, Alaska 99612
    </address>

    <ul class="contact-list">
      <li>
        <svg viewBox="0 0 24 24" aria-hidden="true"><path d="M6.6 10.8a15.1 15.1 0 0 0 6.6 6.6l2.2-2.2c.3-.3.7-.4 1-.2 1.1.4 2.3.6 3.6.6.6 0 1 .4 1 1V20c0 .6-.4 1-1 1A17 17 0 0 1 3 4c0-.6.4-1 1-1h3.5c.6 0 1 .4 1 1 0 1.3.2 2.5.6 3.6.1.3 0 .7-.2 1z"/></svg>
        <span>+1-907-555-2964</span>
      </li>
      <li>
        <svg viewBox="0 0 24 24" aria-hidden="true"><path d="M3 5h18a1 1 0 0 1 1 1v12a1 1 0 0 1-1 1H3a1 1 0 0 1-1-1V6a1 1 0 0 1 1-1zm9 7.5L4.5 7v10h15V7z"/></svg>
        <span>dhalloway@terrainadvisors-example.com</span>
      </li>
      <li>
        <svg viewBox="0 0 24 24" aria-hidden="true"><path d="M12 2a10 10 0 1 0 0 20 10 10 0 0 0 0-20zm6.9 9h-3a15 15 0 0 0-1.2-5.6A8 8 0 0 1 18.9 11zM12 4c1 1.3 1.8 3.9 1.9 7h-3.8C10.2 7.9 11 5.3 12 4zM9.3 5.4A15 15 0 0 0 8.1 11h-3a8 8 0 0 1 4.2-5.6zM5.1 13h3a15 15 0 0 0 1.2 5.6A8 8 0 0 1 5.1 13zM12 20c-1-1.3-1.8-3.9-1.9-7h3.8c-.1 3.1-.9 5.7-1.9 7zm2.7-1.4a15 15 0 0 0 1.2-5.6h3a8 8 0 0 1-4.2 5.6z"/></svg>
        <span>www.willowcrestterrainadvisors-example.com</span>
      </li>
    </ul>
  </section>
</main>
</body>
</html>
```